Plumbing Company After Business Card

Business card for a plumbing business that offers a variety of plumbing services including maintenance, domestic and commercial plumbing. My main focus is to offer high quality professional service. A logo on the card would be ideal. Any other questions feel free to email. Cheers

Looking for something modern and upmarket with preferably a matte black background

Business name is Crestline Plumbing and Gas

Industry/Entity Type

Plumbing

Contact Information for Business Card

Crestline Plumbing and Gas
Marcus Thorvale
0472519306
14 Karrabee Lane, Brindlemoor 3612
crestlineplumbing@mailbay.com.au
ABN 64 915 207 338

Font styles to use
Sans Serif

Colors
1b1b1b
ffffff
3377b5

Requirements
Must have
• Domestic
• Commercial
• Maintenance

```html
<!DOCTYPE html>
<html lang="en">
<head>
<meta charset="utf-8">
<title>Crestline Plumbing and Gas – Business Card</title>
<link rel="stylesheet" href="https://fonts.googleapis.com/css2?family=Open+Sans:wght@400;600;700&display=swap">
<style>
  :root {
    --backdrop: #4b4b4b;
    --card-black: #1b1b1b;
    --brand-blue: #0d5bc6;
    --brand-blue-deep: #0a3f93;
    --brand-blue-light: #2f7fd6;
    --flame-red: #e8402a;
    --flame-orange: #f7a21b;
    --text-white: #ffffff;
    --text-soft: #d9d9d9;
    --divider: #5a5a5a;
  }
  html, body {
    margin: 0;
    padding: 0;
    width: 1105px;
    height: 1200px;
    overflow: hidden;
    background: var(--backdrop);
    font-family: "Open Sans", Arial, sans-serif;
  }
  .canvas {
    position: relative;
    width: 1105px;
    height: 1200px;
  }
  .card {
    position: absolute;
    left: 196px;
    width: 720px;
    height: 412px;
    overflow: hidden;
  }
  .card-front {
    top: 146px;
    background: var(--card-black);
  }
  .card-back {
    top: 602px;
    background: radial-gradient(ellipse at 50% 45%, var(--brand-blue) 0%, var(--brand-blue-deep) 100%);
  }

  /* Front: brand block */
  .brand {
    position: absolute;
    left: 75px;
    top: 164px;
    width: 240px;
    display: flex;
    align-items: center;
    gap: 12px;
  }
  .brand-dot {
    flex: none;
    width: 40px;
    height: 40px;
    border-radius: 50%;
    background: var(--brand-blue);
  }
  .brand-name {
    margin: 0;
    font-size: 20px;
    line-height: 1.25;
    font-weight: 700;
    color: var(--brand-blue-light);
    white-space: nowrap;
  }
  .divider {
    position: absolute;
    left: 333px;
    top: 110px;
    width: 1px;
    height: 170px;
    background: var(--divider);
  }

  /* Front: contact details */
  .contact {
    position: absolute;
    left: 367px;
    top: 113px;
    color: var(--text-soft);
  }
  .contact-name {
    margin: 0 0 12px;
    font-size: 24px;
    font-weight: 600;
    letter-spacing: 0.5px;
    color: var(--brand-blue-light);
  }
  .contact-line {
    margin: 0;
    font-size: 18.5px;
    line-height: 31px;
  }
  .contact-line strong {
    font-weight: 700;
    color: var(--text-white);
  }

  /* Front: colour band */
  .band {
    position: absolute;
    left: 0;
    bottom: 0;
    width: 720px;
    height: 28px;
  }

  /* Back */
  .back-mark {
    position: absolute;
    left: 0;
    right: 0;
    top: 95px;
    text-align: center;
  }
  .back-dot {
    display: inline-block;
    width: 124px;
    height: 124px;
    border-radius: 50%;
    background: #0e1a33;
  }
  .back-name {
    margin: 18px 0 0;
    font-size: 22px;
    font-weight: 700;
    color: var(--text-white);
  }
  .services {
    position: absolute;
    left: 0;
    right: 0;
    top: 346px;
    margin: 0;
    text-align: center;
    font-size: 19.5px;
    color: var(--text-white);
  }
  .services .sep {
    color: var(--flame-red);
    padding: 0 4px;
  }
</style>
</head>
<body>
<main class="canvas">
  <section class="card card-front">
    <div class="brand">
      <span class="brand-dot"></span>
      <p class="brand-name">Crestline<br>Plumbing and Gas</p>
    </div>
    <div class="divider"></div>
    <div class="contact">
      <h1 class="contact-name">MARCUS THORVALE</h1>
      <p class="contact-line">14 Karrabee Lane, Brindlemoor 3612</p>
      <p class="contact-line"><strong>Phone :</strong> 047 251 9306</p>
      <p class="contact-line">crestlineplumbing@mailbay.com.au</p>
      <p class="contact-line">ABN 64 915 207 338</p>
    </div>
    <svg class="band" viewBox="0 0 720 28" aria-hidden="true">
      <defs>
        <linearGradient id="bandBlue" x1="0" x2="1" y1="0" y2="0">
          <stop offset="0" stop-color="#0a3f93"/>
          <stop offset="1" stop-color="#0d5bc6"/>
        </linearGradient>
        <linearGradient id="bandFlame" x1="0" x2="1" y1="0" y2="0">
          <stop offset="0" stop-color="#e8402a"/>
          <stop offset="1" stop-color="#f7a21b"/>
        </linearGradient>
      </defs>
      <polygon points="0,0 472,0 463,28 0,28" fill="url(#bandBlue)"/>
      <polygon points="479,0 720,0 720,28 470,28" fill="url(#bandFlame)"/>
    </svg>
  </section>

  <section class="card card-back">
    <div class="back-mark">
      <span class="back-dot"></span>
      <p class="back-name">Crestline Plumbing and Gas</p>
    </div>
    <p class="services">Domestic<span class="sep">|</span>Commercial<span class="sep">|</span>Maintenance</p>
  </section>
</main>
</body>
</html>
```